Packaging design for a reclosable bag for our product

We have a logo, and we need to put it on packaging for our product and while we want the look to be simple, we want it to follow good design principles and also contain spaces for other product descriptions.

There will be 5 sizes at launch so I'd like 5 variations, one for each size.

I've included a few mockups of the type of bag that I made but they are all just rough ideas that I had.

I want the brand to look scientific and methodical and even a bit quirky, as in "wow this is a serious product but also a bit unusual."

```html
<!DOCTYPE html>
<html lang="en">
<head>
<meta charset="utf-8">
<title>NQ4 Bias Lighting – Bag Label, Extra Large</title>
<link rel="stylesheet" href="https://fonts.googleapis.com/css2?family=Jost:wght@500;700&family=Questrial&display=swap">
<style>
  :root {
    --ink: #000000;
    --paper: #ffffff;
    --backdrop: #f3f3f3;
    --label-shadow: rgba(0, 0, 0, 0.28);
  }
  html, body {
    margin: 0;
    padding: 0;
    width: 1200px;
    height: 963px;
    overflow: hidden;
    background: var(--backdrop);
  }
  .canvas {
    position: relative;
    width: 1200px;
    height: 963px;
    display: flex;
    align-items: center;
    justify-content: center;
  }
  .bag-label {
    width: 685px;
    height: 887px;
    display: block;
    filter: drop-shadow(10px 12px 14px var(--label-shadow));
  }
  .label-ground { fill: var(--ink); }
  .brand-band { fill: var(--paper); }
  .size-box { fill: var(--paper); }
  .brand-name {
    fill: var(--ink);
    font-family: "Jost", sans-serif;
    font-weight: 700;
    font-size: 300px;
  }
  .product-line {
    fill: var(--ink);
    font-family: "Questrial", sans-serif;
    font-size: 55px;
  }
  .spec-text {
    fill: var(--paper);
    font-family: "Jost", sans-serif;
    font-weight: 500;
    font-size: 24px;
    letter-spacing: 0.8px;
  }
  .size-text {
    fill: var(--ink);
    font-family: "Jost", sans-serif;
    font-weight: 500;
    font-size: 27px;
    letter-spacing: 1px;
  }
</style>
</head>
<body>
<main class="canvas">
  <svg class="bag-label" viewBox="0 0 556 720" xmlns="http://www.w3.org/2000/svg" aria-label="NQ4 Bias Lighting bag label, extra large 5 meters">
    <rect class="label-ground" x="0" y="0" width="556" height="720"/>
    <polygon class="brand-band" points="14,113 556,25 556,433 14,538"/>

    <g class="brand-block">
      <text class="brand-name" x="20" y="400" textLength="520" lengthAdjust="spacingAndGlyphs" transform="rotate(-9 20 400)">NQ4</text>
      <text class="product-line" x="86" y="488" transform="rotate(-11 86 488)">Bias Lighting</text>
    </g>

    <g class="spec-block">
      <text class="spec-text" x="54" y="588">Simulated D65</text>
      <text class="spec-text" x="54" y="620">CRI 90+ 6500K</text>
      <text class="spec-text" x="54" y="652">white Bias Lighting</text>
    </g>

    <rect class="size-box" x="352" y="508" width="204" height="212"/>
    <g class="size-block" text-anchor="middle">
      <text class="size-text" x="454" y="590">EXTRA</text>
      <text class="size-text" x="454" y="623">LARGE</text>
      <text class="size-text" x="454" y="657">5 METERS</text>
    </g>
  </svg>
</main>
</body>
</html>
```